Website redesign for Root and Renew

We would like to update the design of our current website to a more concise, conversion optimized design.
The goal of our website is to get our message across as concisely as possible plus encourage people to contact us for more information or to book a consultation.
We need a redesign of the home page and 1 internal page - just for design/layout purposes/format purposes.

Target Market(s)

Males 20-45 years old who are concerned about hair loss and who want to regrow their own hair.

Industry/Entity Type

Health And Wellness

Number of Pages Required

2 page

Font styles to use
Sans Serif

Colors
00a990
33a6d7
ffffff
9d9d9d

Requirements
Must have
• We want the home page to be very concise and to the point in getting the message across. We want to get across the following 6 key messages:
• 1. Dr Brambury story – why he created this solution
• 2. Hair loss is caused by a chemical imbalance
• 3. Root and renew conducts genetic and DNA analysis, then rebalances body chemistry, thus reversing the hair loss process and enabling your own hair to regrow naturally
• 4. Money back guaranteed results
• 5. Purely The Core ingredients – no harsh preservatives or chemicals are included
• 6. All ingredients are FDA approved and safe – no side effects
• We also need a strong call to action. We want people to call or email us to find out more information or to schedule a consultation.
• Here is our current website which is not performing as we would hope: http://www.rootandrenewhq.com/
• Here is our press release for further information: https://www.pressflarex.com/news/finally-we-now-have-a-cure-for-male-pattern-baldness-40528316
• I uploaded the logo files, but let me know if anything else is needed and I can add it.

```html
<!DOCTYPE html>
<html lang="en">
<head>
<meta charset="utf-8">
<title>Root and Renew — Home</title>
<link href="https://fonts.googleapis.com/css2?family=Raleway:wght@300;400;500;600;700;800&display=swap" rel="stylesheet">
<style>
:root{
  --blue:#33a6d7;
  --teal:#00a990;
  --white:#ffffff;
  --grey:#9d9d9d;
  --panel:#eeeeee;
  --card:#f4f4f4;
}
*{box-sizing:border-box;margin:0;padding:0}
html,body{width:1200px;height:2601px;overflow:hidden}
body{position:relative;font-family:'Raleway',Arial,sans-serif;background:var(--white);color:var(--grey)}

/* header */
.site-header{position:absolute;left:0;top:0;width:1200px;height:137px;background:var(--blue)}
.brand{position:absolute;left:109px;top:42px;display:flex;align-items:flex-start;gap:12px;color:var(--white)}
.brand-dot{width:34px;height:34px;border-radius:50%;background:var(--white);margin-top:4px}
.brand-name{font-size:30px;font-weight:500;line-height:34px}
.brand-sub{font-size:17px;font-weight:500;text-align:right;border-top:1.5px solid var(--white);margin-top:4px;padding-top:2px}
.main-nav{position:absolute;top:66px;left:0;height:71px;width:1200px}
.main-nav a{position:absolute;top:0;height:71px;line-height:48px;font-size:15px;font-weight:500;color:var(--white);text-decoration:none}
.main-nav a.active{background:var(--white);color:var(--blue);text-align:center}
.call-pill{position:absolute;left:891px;top:0;width:200px;height:49px;background:var(--white);border-radius:0 0 24px 24px;color:var(--teal);font-size:15px;font-weight:500;text-align:center;line-height:52px}

/* hero */
.hero{position:absolute;left:0;top:137px;width:1200px;height:536px;
  background:linear-gradient(90deg,#a7abad 0%,#c39a82 30%,#b98a6f 48%,#8a8e90 70%,#c6a58f 88%,#6f7679 100%)}
.hero-shade{position:absolute;inset:0;background:linear-gradient(180deg,rgba(40,40,40,.15),rgba(40,40,40,.25))}
.hero-title{position:absolute;top:257px;width:1200px;text-align:center;color:var(--white);font-size:50px;font-weight:800;letter-spacing:1px}
.hero-sub{position:absolute;top:313px;width:1200px;text-align:center;color:var(--white);font-size:38px;font-weight:300}
.hero-tag{position:absolute;top:363px;width:1200px;text-align:center;color:var(--blue);font-size:19px;font-weight:700}
.btn-ghost{position:absolute;left:465px;top:466px;width:272px;height:58px;border:2.5px solid var(--white);border-radius:3px;color:var(--white);font-size:13px;font-weight:700;letter-spacing:1px;text-align:center;line-height:53px}

/* messages */
.messages{position:absolute;left:0;top:673px;width:1200px;height:588px;background:var(--panel)}
.msg-card{position:absolute;z-index:2;width:309px;background:var(--card);box-shadow:0 1px 3px rgba(0,0,0,.08)}
.msg-head{height:70px;background:var(--blue);color:var(--white);font-size:24px;font-weight:400;display:flex;align-items:center;justify-content:center;gap:18px}
.msg-head::before,.msg-head::after{content:"";width:30px;height:2px;background:var(--white)}
.msg-body{padding:30px 30px 0;font-size:13px;line-height:22px;font-weight:600;color:var(--grey);text-align:center}
.msg-link{position:absolute;left:0;width:100%;text-align:center;font-size:13px;font-weight:600;color:var(--blue)}
.inline-link{color:var(--blue)}

/* testimonial */
.stories{position:absolute;left:0;top:1261px;width:1200px;height:652px;background:var(--blue)}
.stories-title{position:absolute;top:107px;width:1200px;text-align:center;color:var(--white);font-size:30px;font-weight:700;line-height:38px}
.video{position:absolute;left:413px;top:218px;width:426px;height:267px;background:#0d0d0d}
.video-frame{position:absolute;left:0;top:14px;width:426px;height:237px;background:linear-gradient(90deg,#7c8c8e 0%,#b98a70 45%,#d6b49d 60%,#e4e4e0 100%)}
.play{position:absolute;left:193px;top:117px}
.video-caption{position:absolute;left:413px;top:522px;width:426px;text-align:center;color:#e3f3fa;font-size:12.5px;font-weight:600;line-height:17.5px}
.video-caption b{color:var(--white)}

/* live tab */
.live-tab{position:absolute;z-index:3;left:0;top:480px;width:47px;height:312px;background:var(--white);border:1px solid #cfcfcf;border-left:none;box-shadow:2px 2px 4px rgba(0,0,0,.15)}
.live-tab span{position:absolute;left:23px;top:140px;transform:translate(-50%,-50%) rotate(-90deg);white-space:nowrap;color:var(--teal);font-size:10.5px;font-weight:600;letter-spacing:1.2px}
.live-tab i{position:absolute;left:8px;bottom:10px;width:28px;height:28px;border-radius:5px;background:var(--teal)}

/* faqs */
.faqs{position:absolute;left:0;top:1913px;width:1200px;height:416px;background:var(--panel)}
.faqs-title{position:absolute;top:58px;width:1200px;text-align:center;color:var(--blue);font-size:30px;font-weight:400}
.faq{position:absolute;top:125px;width:433px}
.faq h3{color:var(--blue);font-size:24px;font-weight:600;margin-bottom:18px}
.faq p{color:var(--blue);font-size:13px;font-weight:400;line-height:26px}
.faq-more{position:absolute;left:659px;top:356px;color:var(--blue);font-size:14px;font-weight:700}

/* footer */
.site-footer{position:absolute;left:0;top:2329px;width:1200px;height:272px;background:var(--blue);color:var(--white)}
.f-col{position:absolute;top:52px;font-size:13.5px;font-weight:500;line-height:17px}
.f-col h4{font-size:14px;font-weight:700;margin-bottom:17px}
.field{position:absolute;background:#f2f2f2;border-radius:7px;color:var(--grey);font-size:13px;padding:6px 12px}
.send{position:absolute;left:635px;top:198px;width:128px;height:28px;border:1.5px solid var(--white);border-radius:14px;font-size:11.5px;text-align:center;line-height:25px}
.social{position:absolute;top:201px;width:28px;height:28px;border-radius:50%;background:var(--white)}
</style>
</head>
<body>

<header class="site-header">
  <div class="brand">
    <div class="brand-dot"></div>
    <div>
      <div class="brand-name">Root &amp; Renew</div>
      <div class="brand-sub">by Robert Brambury M.D.</div>
    </div>
  </div>
  <nav class="main-nav">
    <a style="left:503px">ABOUT US</a>
    <a style="left:620px">HOW IT WORKS</a>
    <a class="active" style="left:753px;width:78px">BLOG</a>
    <a style="left:858px">SALON PARTNERS</a>
    <a style="left:1027px">CONTACT</a>
  </nav>
  <div class="call-pill">CALL US: (310) 555-0186</div>
</header>

<section class="hero" role="img" aria-label="Photo of a young man checking his receding hairline in a bathroom mirror">
  <div class="hero-shade"></div>
</section>
<h1 class="hero-title">THE REVOLUTIONARY NEW SOLUTION</h1>
<p class="hero-sub">FOR HAIR LOSS THAT USES PERSONALIZED MEDICINE</p>
<p class="hero-tag">The First Non-Surgical Hair Loss Solution With Clinically Proven Results And 100% Money Back Guarantee!</p>
<div class="btn-ghost">SCHEDULE A CONSULTATION</div>

<section class="messages"></section>

<section class="stories">
  <h2 class="stories-title">Our clients love keeping and growing their hair back.<br>You can too!</h2>
  <div class="video">
    <div class="video-frame" role="img" aria-label="Video still of a client in an orange shirt telling his story"></div>
    <svg class="play" width="40" height="30" viewBox="0 0 40 30"><rect width="40" height="30" rx="6" fill="#111" opacity=".85"/><path d="M16 9 L26 15 L16 21 Z" fill="#fff"/></svg>
  </div>
  <p class="video-caption">Marcus first came to see me four months ago. Here he tells the story about how he first realized he was receding and losing his hair as well as his experience with the Root and Renew personalized program so far.<br>Read more <b>Success Stories</b></p>
</section>

<article class="msg-card" style="left:111px;top:629px;height:321px">
  <div class="msg-head">THE STORY</div>
  <p class="msg-body">Dr. Robert Brambury, the creator of Root and Renew is a renowned hair restoration expert. After seeing first his father and then older brothers thin and go bald, he dedicated his life to finding the cure for hair loss.</p>
  <a class="msg-link" style="top:278px">Read more of Dr Brambury story here.</a>
</article>
<article class="msg-card" style="left:446px;top:629px;height:321px">
  <div class="msg-head">THE CAUSE</div>
  <p class="msg-body">The vast majority of cases we see do have at least some component of hereditary baldness as part of the mix. The reason it is hereditary is due to a small defect on one (hereditary) gene which causes our bodies to over-produce the hormone DHT.</p>
  <a class="msg-link" style="top:278px">How stopping hair loss can save your life.</a>
</article>
<article class="msg-card" style="left:780px;top:629px;height:321px">
  <div class="msg-head">THE SOLUTION</div>
  <p class="msg-body" style="text-align:left">Root and renew conducts genetic and DNA analysis, then rebalances body chemistry, thus reversing the hair loss process and enabling your own hair to regrow naturally.</p>
  <a class="msg-link" style="top:278px">How stopping hair loss can save your life.</a>
</article>

<article class="msg-card" style="left:111px;top:988px;height:321px">
  <div class="msg-head">THE GARANTEE</div>
  <p class="msg-body" style="text-align:left">Dr. Brambury is so confident of the effectiveness of this solution he is providing <span class="inline-link">his personal guarantee</span>.</p>
</article>
<article class="msg-card" style="left:446px;top:988px;height:321px">
  <div class="msg-head">THE INGREDIENTS</div>
  <p class="msg-body" style="text-align:left;padding-top:24px">&nbsp; &nbsp; &nbsp; Purely The Core ingredients – no harsh preservatives or chemicals are included. Dr. Brambury created his solution from a combination of FDA-approved active ingredients. The combination of medicines we use are clinically proven to both block DHT and stimulate hair growth. <span class="inline-link">You can find more details on this here.</span></p>
</article>
<article class="msg-card" style="left:780px;top:988px;height:321px">
  <div class="msg-head">NO SIDE EFFECTS</div>
  <p class="msg-body" style="text-align:left">All ingredients are FDA approved and safe. We have had zero side effects reported to either us or the pharmacy. Dr Brambury personalizes your dose based on your DNA and THAT makes all the difference. You can read more about it <span class="inline-link">here</span>.</p>
</article>

<aside class="live-tab"><span>LIVE REPRESENTATIVE AVAILABLE</span><i></i></aside>

<section class="faqs">
  <h2 class="faqs-title">QUICK FAQS</h2>
  <div class="faq" style="left:165px">
    <h3>How Much Does It Cost?</h3>
    <p>For just a small monthly charge, we will provide you with your personalized solution. The cost will vary depending on the stage of your hair thinning or loss and your genetic make-up. Typical monthly costs range between $99 up to $199 per month depending on how severe your case is plus there is a discount for paying annually in advance. There is also a fee for your lab tests if you do not have insurance to cover this. Tax deductions may also apply for some patients.</p>
  </div>
  <div class="faq" style="left:659px">
    <h3>How long does it take?</h3>
    <p>After three to six months you will start to see hair loss stop. After 6 to 9 months you will start to see your hair regrow. It is important to act before any of your hair follicles die. Once they have died they cannot be regrown.</p>
  </div>
  <a class="faq-more">Read more Frequently Asked Questions.</a>
</section>

<footer class="site-footer">
  <div class="f-col" style="left:111px">
    <h4>Address</h4>
    Root and Renew Hair, LLC<br>4417 Cedarline Blvd, Suite 300<br>Larkspur Hills CA 90390
  </div>
  <div class="f-col" style="left:364px">
    <h4>Hours of Operation</h4>
    Monday - Friday: 9.00am to 5.00pm<br>Saturday: 8.00am to 2.00pm<br>Call Us (310) 555-0186<br>&nbsp;(310) 555-0186
  </div>
  <div class="f-col" style="left:636px"><h4>Have more question? Email us!</h4></div>
  <div class="field" style="left:636px;top:76px;width:201px;height:30px">Your Name...</div>
  <div class="field" style="left:857px;top:76px;width:199px;height:30px">Your e-mail...</div>
  <div class="field" style="left:636px;top:116px;width:420px;height:70px">Message...</div>
  <div class="send">Send message</div>
  <span class="social" style="left:111px;border-radius:5px"></span>
  <span class="social" style="left:163px"></span>
  <span class="social" style="left:217px;border-radius:5px"></span>
  <span class="social" style="left:269px"></span>
</footer>

</body>
</html>
```